After tattoo calming solution

The label has to be modern, along the same lines as skin care brand “Plain Form.” It has to reflect the solutions natural effectiveness and simplicity. The label cannot be over fussy, and must be a little bit clinical, as it really does work. The colours should reflect that the solution calms the skin.

We use a 100ml spray bottle.

Target Market(s)

Anyone with a new tattoo or piercing

Industry/Entity Type

Skincare

Requirements
Must have
• Must reflect its natural calming but still remain a little clinical
Should not have
• It must not look like other flowery tattoo cream solutions.

```html
<!DOCTYPE html>
<html lang="en">
<head>
<meta charset="utf-8">
<title>Quiet Skin – 100ml spray label</title>
<link rel="stylesheet" href="https://fonts.googleapis.com/css2?family=Outfit:wght@400;500&display=swap">
<style>
  :root {
    --backdrop: #f5f5f5;
    --label: #ffffff;
    --ink: #1c1c1c;
    --nude: #f7cdd0;
  }
  * { box-sizing: border-box; margin: 0; padding: 0; }
  html, body {
    width: 1200px;
    height: 846px;
    overflow: hidden;
    background: var(--backdrop);
  }
  .canvas {
    position: relative;
    width: 1200px;
    height: 846px;
  }
  .label {
    position: absolute;
    left: 397px;
    top: 73px;
    width: 406px;
    height: 700px;
    background: var(--label);
    box-shadow: 0 1px 3px rgba(0,0,0,0.06);
    color: var(--ink);
    font-family: "Outfit", sans-serif;
    text-align: center;
  }
  .brand-name {
    position: absolute;
    top: 52px;
    left: 0;
    right: 0;
    font-weight: 400;
    font-size: 56px;
    line-height: 0.95;
    letter-spacing: 0.04em;
    text-transform: uppercase;
  }
  .tagline {
    position: absolute;
    top: 352px;
    left: 0;
    right: 0;
    font-weight: 500;
    font-size: 35px;
    line-height: 1.3;
    letter-spacing: -0.035em;
  }
  .nude-rule {
    position: absolute;
    top: 509px;
    left: 50%;
    width: 140px;
    height: 5px;
    margin-left: -70px;
    background: var(--nude);
  }
  .benefits {
    position: absolute;
    top: 536px;
    left: 0;
    right: 0;
    font-weight: 400;
    font-size: 20px;
    line-height: 1.23;
    letter-spacing: -0.03em;
  }
  .volume {
    position: absolute;
    top: 648px;
    left: 0;
    right: 0;
    font-weight: 400;
    font-size: 21px;
    letter-spacing: -0.02em;
  }
</style>
</head>
<body>
  <main class="canvas">
    <section class="label">
      <h1 class="brand-name">Quiet<br>Skin</h1>
      <p class="tagline">Expert skin repair<br>for new tattoos<br>&amp; piercings</p>
      <div class="nude-rule"></div>
      <p class="benefits">Reduces inflamation,<br>irritation &amp; encourages<br>natural skin healing</p>
      <p class="volume">100ml</p>
    </section>
  </main>
</body>
</html>
```